Polish brewery needs BEER LABEL design for WEDDINGS

We need beer label design for weddings. Our brewery is located on South of Poland and it is called Zakład Wrzos [PL]/Heather Works [ENG]. We feel strong connection to mountains and we use water from the mountain in our vicinity.
Regarding beer style it is India Pale Ale so beer is bitter and aromatic because of high addition of hops. Label design has to be modern and simple. We would prefer bright and cream colors.
We need to have opportunity to edit data which are on the label so we will need to get appropriate files.
In attached files you can find all details. If any additional information will be required please do not hesitate and contact with me.

Target Market(s)

Weddings

Font styles to use
Sans Serif
Script

Colors
ffffff

Requirements
Must have
• Information listed in documents in attached files
Nice to have
• Some nice graphics
Bright and cream colors.
Should not have
• -

```html
<!DOCTYPE html>
<html lang="pl">
<head>
<meta charset="utf-8">
<title>Bride + Groom – India Pale Ale</title>
<link href="https://fonts.googleapis.com/css2?family=Montserrat:wght@400;500;700&family=Cormorant+Garamond:wght@500&display=swap" rel="stylesheet">
<style>
  :root {
    --cream: #fffdd3;
    --ink: #1c1410;
    --tiger: #dc8a1f;
    --leaf: #1f7a3c;
    --hop-pale: #d8cf9a;
    --brand: #8a7146;
  }
  html, body { margin: 0; padding: 0; overflow: hidden; }
  body { width: 1200px; height: 534px; background: var(--cream); }
  .label {
    position: relative; width: 1200px; height: 534px; overflow: hidden;
    background: var(--cream); color: var(--ink);
    font-family: "Montserrat", sans-serif;
  }
  .abs { position: absolute; margin: 0; }

  /* left panel */
  .ingredients { left: 40px; top: 62px; font-size: 19px; line-height: 23px; width: 330px; }
  .storage { left: 40px; top: 176px; font-size: 16px; line-height: 14px; width: 330px; }
  .storage p { margin: 0 0 14px; }
  .storage .volume { margin-top: 14px; }
  .storage strong { font-weight: 700; }
  .producer { left: 40px; top: 348px; font-size: 14px; line-height: 19px; }
  .producer p { margin: 0; }
  .brand-mark {
    left: 296px; top: 380px; width: 70px; text-align: center;
    font-size: 9px; font-weight: 700; color: var(--brand); line-height: 10px;
  }

  /* centre */
  .art { border-radius: 50%; opacity: .55; }
  .art-tiger-top { left: 662px; top: 12px; width: 112px; height: 305px;
    background: linear-gradient(160deg, var(--tiger), #c9781a); border-radius: 45% 45% 50% 50%; }
  .art-leaf-top { left: 415px; top: 58px; width: 170px; height: 175px;
    background: radial-gradient(circle at 70% 30%, var(--leaf), #2f8f4c 70%); border-radius: 60% 20% 60% 20%; opacity: .35; }
  .art-tiger-bottom { left: 392px; top: 224px; width: 222px; height: 248px;
    background: linear-gradient(200deg, var(--tiger), #c9781a); border-radius: 40% 50% 45% 55%; }
  .art-leaf-bottom { left: 616px; top: 330px; width: 136px; height: 134px;
    background: radial-gradient(circle at 30% 70%, var(--leaf), #2f8f4c 70%); border-radius: 20% 60% 20% 60%; opacity: .35; }

  .title {
    left: 490px; width: 216px; text-align: center;
    font-family: "Cormorant Garamond", serif; font-weight: 500; letter-spacing: .32em;
    color: var(--ink);
  }
  .title-bride { top: 188px; font-size: 32px; }
  .title-plus { top: 224px; font-size: 28px; letter-spacing: 0; }
  .title-groom { top: 252px; font-size: 32px; }
  .date { left: 500px; width: 200px; top: 337px; text-align: center; font-size: 11px; letter-spacing: .32em; }
  .style { left: 480px; width: 240px; top: 494px; text-align: center; font-size: 14px; letter-spacing: .3em; font-weight: 500; }

  /* right panel */
  .story { left: 841px; top: 34px; width: 330px; font-size: 16px; line-height: 19.7px; }
  .scale-label { font-size: 9px; top: 209px; width: 60px; text-align: center; }
  .scale-bitter { left: 874px; }
  .scale-color { left: 980px; }
  .stat { top: 306px; font-size: 22px; font-weight: 700; width: 80px; text-align: center; }
  .stat-abv { left: 913px; }
  .stat-ibu { left: 1027px; }
  .icons { left: 865px; top: 220px; }

  .social { left: 843px; top: 392px; font-size: 17px; font-weight: 500; }
  .social li { list-style: none; display: flex; align-items: center; height: 28px; }
  .social ul { margin: 0; padding: 0; }
  .social .dot { width: 18px; height: 18px; border: 1.6px solid var(--ink); border-radius: 50%; box-sizing: border-box; margin-right: 12px; }
</style>
</head>
<body>
<main class="label">
  <!-- left -->
  <p class="abs ingredients">Składniki: woda, słód jęczmienny, chmiel, liście limonki, drożdże.</p>
  <div class="abs storage">
    <p>Najlepiej spożyć przed:</p>
    <p>Przechowywać w suchym i chłodnym miejscu</p>
    <p class="volume">Objętość butelki:&nbsp; <strong>330ml</strong></p>
  </div>
  <div class="abs producer">
    <p>Zakład Wrzos</p>
    <p>34-512 Wrzosowa Dolina</p>
    <p>Browar Górski Halny</p>
    <p>Halna 48, 34-630 Jodłowa Wola</p>
  </div>
  <div class="abs brand-mark">ZAKŁAD WRZOS</div>

  <!-- centre artwork -->
  <div class="abs art art-leaf-top" role="img" aria-label="Green leafy branch curving around the top left of the wreath"></div>
  <div class="abs art art-tiger-top" role="img" aria-label="Illustrated orange striped tiger climbing down the right side"></div>
  <div class="abs art art-tiger-bottom" role="img" aria-label="Illustrated orange striped tiger stretching along the lower left"></div>
  <div class="abs art art-leaf-bottom" role="img" aria-label="Green leafy branch curving around the bottom right of the wreath"></div>

  <div class="abs title title-bride">BRIDE</div>
  <div class="abs title title-plus">+</div>
  <div class="abs title title-groom">GROOM</div>
  <div class="abs date">10.11.20XX</div>
  <div class="abs style">India Pale Ale</div>

  <!-- right -->
  <p class="abs story">Trzymasz w ręku naszą autorską IPA do produkcji której wykorzystujemy wodę wypływającą z samego serca Beskidu Wysokiego – Babiej Góry. IPA lubi chmiele i goryczkę, ale żeby nie było nudno postanowiliśmy ją wzbogacić limonką.</p>

  <div class="abs scale-label scale-bitter">Bitterness</div>
  <div class="abs scale-label scale-color">Color</div>
  <svg class="abs icons" width="260" height="50" viewBox="0 0 260 50" aria-hidden="true">
    <g>
      <ellipse cx="14" cy="24" rx="9" ry="12" fill="var(--ink)"/>
      <ellipse cx="39" cy="24" rx="9" ry="12" fill="var(--ink)"/>
      <ellipse cx="64" cy="24" rx="9" ry="12" fill="var(--hop-pale)"/>
    </g>
    <g stroke-width="5" stroke-linecap="round">
      <line x1="118" y1="10" x2="118" y2="42" stroke="var(--ink)"/>
      <line x1="145" y1="10" x2="145" y2="42" stroke="var(--hop-pale)"/>
      <line x1="172" y1="10" x2="172" y2="42" stroke="var(--hop-pale)"/>
    </g>
    <path d="M241 1 C236 12 228 20 228 30 A13 13 0 0 0 254 30 C254 20 246 12 241 1 Z" fill="var(--ink)"/>
  </svg>
  <div class="abs stat stat-abv">5.5%</div>
  <div class="abs stat stat-ibu">14%</div>

  <div class="abs social">
    <ul>
      <li><span class="dot"></span>zakladwrzos</li>
      <li><span class="dot"></span>zaklad.wrzos</li>
      <li><span class="dot"></span>www.zakladwrzos.pl</li>
    </ul>
  </div>
</main>
</body>
</html>
```